study by ripples circle

The website presents a new interactive learning system where it provides not only the teaching material as the instructor friend who can both teach and learn, making friends and making money.
Make friends and get money.

```html
<!DOCTYPE html>
<html lang="en">
<head>
<meta charset="utf-8">
<title>study by ripples circle</title>
<link href="https://fonts.googleapis.com/css2?family=Oswald:wght@400;600&family=Open+Sans:wght@400;600&display=swap" rel="stylesheet">
<style>
:root{
  --navy:#1b2944;
  --blue:#1f5ca8;
  --deep:#1d3b78;
  --sky:#3e8fd6;
  --paper:#ffffff;
  --beige:#e6dac3;
  --ink:#3a3f4a;
  --muted:#7a808c;
  --line:#d7dbe2;
  --footer:#f3f4f6;
}
*{box-sizing:border-box;margin:0;padding:0}
html,body{width:756px;height:1200px;overflow:hidden}
body{background:var(--beige);font-family:"Open Sans",sans-serif;color:var(--ink);position:relative}
.topbar{position:absolute;left:0;top:0;width:756px;height:22px;background:var(--navy);display:flex;justify-content:center;align-items:center;gap:6px}
.topbar span{width:11px;height:11px;border-radius:50%;background:#8ea3c7}
.navbar{position:absolute;left:0;top:22px;width:756px;height:92px;background:var(--paper);border-bottom:3px solid var(--blue)}
.nav{position:absolute;top:26px;display:flex;gap:18px;font-family:"Oswald",sans-serif;font-size:11px;color:var(--deep);letter-spacing:.5px}
.nav.left{left:168px}.nav.right{left:446px}
.nav a{color:inherit;text-decoration:none}
.nav a.active{border-bottom:2px solid var(--blue);padding-bottom:2px}
.brand{position:absolute;left:0;width:756px;top:14px;text-align:center}
.brand .mark{display:block;width:26px;height:26px;border-radius:50%;background:var(--blue);margin:0 auto 6px}
.brand .name{font-family:"Oswald",sans-serif;font-weight:600;font-size:15px;color:var(--deep);letter-spacing:.5px}
.hero{position:absolute;left:40px;top:122px;width:676px;height:344px;background:var(--paper);box-shadow:0 8px 10px -6px rgba(0,0,0,.35)}
.hero-art{position:absolute;inset:8px;background:linear-gradient(120deg,#dfe4ea 0%,#f4f6f8 35%,#d9ecf8 60%,#f7e4c8 100%)}
.hero-title{position:absolute;right:40px;top:216px;text-align:center;font-family:"Oswald",sans-serif;font-size:30px;line-height:36px;color:var(--deep)}
.slide-arrow{position:absolute;top:270px;width:20px;height:30px;background:var(--deep)}
.slide-arrow.prev{left:40px}.slide-arrow.next{right:40px}
.slide-arrow svg{width:20px;height:30px}
.about{position:absolute;left:40px;top:480px;width:676px;height:250px;background:var(--paper);padding:18px 20px}
h2{font-family:"Oswald",sans-serif;font-weight:600;font-size:18px;color:var(--blue);letter-spacing:1px;text-align:center;position:relative}
.about-col{position:absolute;top:16px;width:310px}
.about-col.intro{left:20px}.about-col.team{left:350px}
.intro .pic{position:absolute;left:0;top:36px;width:110px;height:96px;background:linear-gradient(135deg,#2b5f9a,#6fa6d8)}
.intro p{position:absolute;left:122px;top:36px;width:188px;font-size:9px;line-height:14px;color:var(--muted)}
.intro .more{left:120px;top:172px}
.btn{position:absolute;background:var(--deep);color:#fff;font-family:"Oswald",sans-serif;font-size:10px;letter-spacing:.5px;padding:5px 14px}
.members{position:absolute;top:36px;left:0;width:310px;display:flex;justify-content:space-between}
.member{width:96px;text-align:center}
.member .avatar{width:56px;height:56px;border-radius:50%;margin:0 auto 6px;background:linear-gradient(135deg,#c9a98a,#e5d2bd)}
.member .dots{display:flex;justify-content:center;gap:4px;margin-bottom:6px}
.member .dots i{width:12px;height:12px;border-radius:50%;background:var(--deep)}
.member h3{font-family:"Oswald",sans-serif;font-size:10px;color:var(--deep);font-weight:400;letter-spacing:.5px}
.member p{font-size:8px;line-height:12px;color:var(--muted);margin-top:4px}
.service{position:absolute;left:40px;top:738px;width:676px;height:224px}
.service-bg{position:absolute;inset:0;background:linear-gradient(100deg,#8c7a6c,#c8b9aa 45%,#7d8a99)}
.service-title{position:absolute;left:248px;top:14px;width:180px;height:30px;background:var(--paper)}
.service-title h2{line-height:30px}
.cards{position:absolute;left:18px;top:62px;width:640px;display:flex;justify-content:space-between}
.card{width:196px;height:140px;background:var(--paper);text-align:center;padding-top:40px;position:relative}
.card .icon{position:absolute;left:78px;top:-16px;width:40px;height:40px;border-radius:50%;background:var(--deep);border:3px solid #fff}
.card .icon svg{width:34px;height:34px}
.card h3{font-family:"Oswald",sans-serif;font-size:12px;color:var(--deep);font-weight:400;letter-spacing:.5px}
.card p{font-size:8px;line-height:12px;color:var(--muted);padding:6px 16px 0}
.card .link{display:block;font-family:"Oswald",sans-serif;font-size:9px;color:var(--blue);margin-top:8px}
.footer{position:absolute;left:40px;top:970px;width:676px;height:202px;background:var(--footer);padding:16px 14px;display:flex;gap:14px}
.footer h4{font-family:"Oswald",sans-serif;font-size:13px;color:var(--blue);letter-spacing:.5px;margin-bottom:8px}
.f-links{width:96px}
.f-links li{list-style:none;font-size:9px;line-height:19px;color:var(--deep)}
.f-links li::before{content:"›";margin-right:6px;color:var(--blue)}
.f-photos{width:130px}
.grid{display:grid;grid-template-columns:repeat(3,38px);gap:4px}
.grid span{height:32px;background:linear-gradient(135deg,#7f95ad,#c9d3dd)}
.f-news{width:120px}
.news{display:flex;gap:6px;margin-bottom:10px}
.news i{width:30px;height:30px;flex:none;background:linear-gradient(135deg,#8aa0b8,#d3dbe3)}
.news p{font-size:8px;line-height:11px;color:var(--muted)}
.news b{display:block;color:var(--deep);font-weight:600}
.f-contact{width:100px}
.field{background:#fff;border:1px solid var(--line);font-size:8px;color:var(--muted);padding:4px 6px;margin-bottom:5px}
.field.msg{height:44px}
.send{display:inline-block;background:var(--deep);color:#fff;font-size:8px;padding:3px 10px;font-family:"Oswald",sans-serif}
.f-address{width:134px;padding-top:22px}
.addr{display:flex;gap:6px;font-size:8px;line-height:11px;color:var(--muted);margin-bottom:12px}
.addr svg{width:12px;height:12px;flex:none}
.copyright{position:absolute;left:0;top:1176px;width:756px;height:24px;background:var(--deep);color:#c9d4ea;font-size:8px;text-align:center;line-height:24px}
</style>
</head>
<body>
<div class="topbar"><span></span><span></span><span></span><span></span><span></span><span></span></div>

<header class="navbar">
  <nav class="nav left"><a class="active">HOME</a><a>ABOUT US</a><a>SERVICE</a></nav>
  <div class="brand"><span class="mark"></span><span class="name">study by ripples circle</span></div>
  <nav class="nav right"><a>SRC</a><a>WHO WE ARE</a><a>CONTACT US</a></nav>
</header>

<section class="hero">
  <div class="hero-art" role="img" aria-label="Young man with glasses beside a laptop bursting with colourful arrows, tools and learning symbols"></div>
  <div class="hero-title">study by ripples<br>circle</div>
</section>
<div class="slide-arrow prev"><svg viewBox="0 0 20 30"><path d="M12 9 6 15l6 6" stroke="#fff" stroke-width="2" fill="none"/></svg></div>
<div class="slide-arrow next"><svg viewBox="0 0 20 30"><path d="M8 9l6 6-6 6" stroke="#fff" stroke-width="2" fill="none"/></svg></div>

<section class="about">
  <div class="about-col intro">
    <h2>ABOUT US</h2>
    <div class="pic" role="img" aria-label="Illustration of a head filled with learning icons"></div>
    <p>Our circle mixes lessons and friendship so every learner can teach, study and grow together. Join short sessions, share notes and earn rewards while you help others move forward in class and in life, one small ripple at a time.</p>
    <span class="btn more">READ MORE</span>
  </div>
  <div class="about-col team">
    <h2>WHO ARE WE ?</h2>
    <div class="members">
      <div class="member"><div class="avatar" role="img" aria-label="Portrait photo of team member"></div><div class="dots"><i></i><i></i><i></i></div><h3>CLARA WENDT</h3><p>Tutor and mentor who guides new members</p></div>
      <div class="member"><div class="avatar" role="img" aria-label="Portrait photo of team member"></div><div class="dots"><i></i><i></i><i></i></div><h3>MILO BARRETT</h3><p>Tutor and mentor who guides new members</p></div>
      <div class="member"><div class="avatar" role="img" aria-label="Portrait photo of team member"></div><div class="dots"><i></i><i></i><i></i></div><h3>JONAS PIKE</h3><p>Tutor and mentor who guides new members</p></div>
    </div>
  </div>
</section>

<section class="service">
  <div class="service-bg" role="img" aria-label="Photo of students studying together at a table"></div>
  <div class="service-title"><h2>OUR SERVICE</h2></div>
  <div class="cards">
    <div class="card"><span class="icon"><svg viewBox="0 0 34 34"><path d="M9 12h16v11H9zM17 12v11" stroke="#fff" stroke-width="1.8" fill="none"/></svg></span><h3>LEARNING</h3><p>Short lessons shaped by friends who teach and learn side by side.</p><span class="link">READ MORE</span></div>
    <div class="card"><span class="icon"><svg viewBox="0 0 34 34"><path d="M9 10h16v10H15l-4 4v-4H9z" stroke="#fff" stroke-width="1.8" fill="none"/></svg></span><h3>SUGGESTION</h3><p>Short lessons shaped by friends who teach and learn side by side.</p><span class="link">READ MORE</span></div>
    <div class="card"><span class="icon"><svg viewBox="0 0 34 34"><path d="M10 18l5 5 9-11" stroke="#fff" stroke-width="2" fill="none"/></svg></span><h3>REPORT YOUR FINDING</h3><p>Short lessons shaped by friends who teach and learn side by side.</p><span class="link">READ MORE</span></div>
  </div>
</section>

<footer class="footer">
  <div class="f-links"><h4>LINKS</h4><ul><li>HOME</li><li>ABOUT US</li><li>SERVICE</li><li>WHO WE ARE</li><li>SRC NEWS</li><li>CONTACT US</li></ul></div>
  <div class="f-photos"><h4>PHOTOS</h4><div class="grid" role="img" aria-label="Gallery of member photos"><span></span><span></span><span></span><span></span><span></span><span></span><span></span><span></span><span></span></div></div>
  <div class="f-news"><h4>SRC NEWS</h4>
    <div class="news"><i role="img" aria-label="News thumbnail"></i><p><b>Weekly meetup notes</b>Posted on May 12, 2024</p></div>
    <div class="news"><i role="img" aria-label="News thumbnail"></i><p><b>New tutor pairs</b>Posted on May 19, 2024</p></div>
    <div class="news"><i role="img" aria-label="News thumbnail"></i><p><b>Reward points update</b>Posted on May 26, 2024</p></div>
  </div>
  <div class="f-contact"><h4>CONTACT US</h4><div class="field">Name</div><div class="field">Email</div><div class="field msg">Message</div><span class="send">Send</span></div>
  <div class="f-address">
    <div class="addr"><svg viewBox="0 0 12 12"><path d="M6 11S2 7 2 4.5a4 4 0 0 1 8 0C10 7 6 11 6 11z" fill="#1f5ca8"/></svg><span>Address: 24 Harbor Lane, Brookfield</span></div>
    <div class="addr"><svg viewBox="0 0 12 12"><path d="M3 1h2l1 3-1.5 1a6 6 0 0 0 2.5 2.5L8 6l3 1v2c0 1-1 2-2 2A8 8 0 0 1 1 3c0-1 1-2 2-2z" fill="#1f5ca8"/></svg><span>(555) 014-2286</span></div>
    <div class="addr"><svg viewBox="0 0 12 12"><path d="M1 3h10v6H1zM1 3l5 4 5-4" stroke="#1f5ca8" fill="none"/></svg><span>hello@ripplescircle.org</span></div>
  </div>
</footer>
<div class="copyright">Copyright 2024 study by ripples circle. All rights reserved</div>
</body>
</html>
```